Mirvane Trinkets
Lucinda Harrow Designs
Mirvane Trinkets -
Creative Brief
Simple
Lucinda Harrow
Jewelry Designer
2719 Quillfern Ln Dallas TX 75294
lucinda@mirvane-example.com
www.mirvane-example.com
Please do a few designs!
Maybe just the logo?

```html
<!DOCTYPE html>
<html lang="en">
<head>
<meta charset="utf-8">
<title>Mirvane Trinkets – Business Card</title>
<link rel="stylesheet" href="https://fonts.googleapis.com/css2?family=Open+Sans:wght@400;600;700&display=swap">
<style>
  :root {
    --backdrop: #ecebe8;
    --card: #ffffff;
    --ink: #6b6b6b;
    --ink-dark: #555555;
    --teal-dark: #139a92;
    --teal-light: #3fd3c6;
    --silver: #c4c4c4;
    --silver-light: #e2e2e2;
  }
  * { margin: 0; padding: 0; box-sizing: border-box; }
  html, body {
    width: 1200px;
    height: 935px;
    overflow: hidden;
    background: var(--backdrop);
    font-family: "Open Sans", sans-serif;
  }
  .canvas {
    position: relative;
    width: 1200px;
    height: 935px;
  }
  .business-card {
    position: absolute;
    left: 100px;
    top: 177px;
    width: 1000px;
    height: 580px;
    background: var(--card);
    border-radius: 44px;
    overflow: hidden;
    box-shadow: 0 6px 24px rgba(0, 0, 0, 0.12);
  }
  .card-swoosh {
    position: absolute;
    left: 0;
    top: 0;
    width: 1000px;
    height: 580px;
  }
  .brand {
    position: absolute;
    left: 0;
    right: 0;
    top: 78px;
    display: flex;
    flex-direction: column;
    align-items: center;
    gap: 22px;
  }
  .brand-dot {
    width: 64px;
    height: 64px;
    border-radius: 50%;
    background: var(--teal-dark);
  }
  .brand-name {
    font-size: 62px;
    font-weight: 600;
    color: var(--ink-dark);
    letter-spacing: 1px;
    line-height: 1;
  }
  .person {
    position: absolute;
    right: 560px;
    top: 370px;
    text-align: right;
    color: var(--ink);
  }
  .person-name {
    font-size: 32px;
    font-weight: 700;
    line-height: 1.2;
  }
  .person-role {
    font-size: 22px;
    font-weight: 600;
    line-height: 1.4;
  }
  .contact {
    position: absolute;
    left: 470px;
    top: 318px;
    list-style: none;
    color: var(--ink);
    font-size: 21px;
    line-height: 1.5;
  }
  .contact-label {
    font-weight: 700;
  }
</style>
</head>
<body>
<main class="canvas">
  <section class="business-card">
    <svg class="card-swoosh" viewBox="0 0 1000 580" aria-hidden="true">
      <defs>
        <linearGradient id="tealBand" x1="0" y1="0" x2="1" y2="1">
          <stop offset="0" stop-color="var(--teal-dark)"/>
          <stop offset="0.55" stop-color="var(--teal-light)"/>
          <stop offset="1" stop-color="var(--teal-dark)"/>
        </linearGradient>
        <linearGradient id="silverBand" x1="0" y1="0" x2="1" y2="1">
          <stop offset="0" stop-color="var(--silver)"/>
          <stop offset="1" stop-color="var(--silver-light)"/>
        </linearGradient>
      </defs>
      <path d="M0,70 C70,300 210,480 440,580 L300,580 C140,480 50,300 0,150 Z" fill="url(#silverBand)"/>
      <path d="M0,150 C50,300 140,480 300,580 L0,580 Z" fill="url(#tealBand)"/>
    </svg>

    <div class="brand">
      <span class="brand-dot"></span>
      <span class="brand-name">Mirvane Trinkets</span>
    </div>

    <div class="person">
      <p class="person-name">Lucinda Harrow</p>
      <p class="person-role">Jewelry Designer</p>
    </div>

    <ul class="contact">
      <li>2719 Quillfern Ln Dallas TX 75294</li>
      <li><span class="contact-label">Phone :</span> 214-555-0137</li>
      <li><span class="contact-label">Email :</span> lucinda@mirvane-example.com</li>
      <li><span class="contact-label">Web :</span> www.mirvane-example.com</li>
    </ul>
  </section>
</main>
</body>
</html>
```